Torvik & Associates - 3rd Party Logistics Company

Torvik & Associates is a 3rd Party Logistics Company established in 1995 located in St. Louis, MO USA. We are a non asset based transportation company that works with our clients to move their freight and help them manage their supply chain. We are looking for a brochure about our company and services. We are able to provide our customers with shipment entry and rating tools along with visibility of all their shipments thought our cloud based TMS build on CloudNest's Pelzo.com platform. Through our TMS application we also provide customized reports, KPI and dashboards specific to the clients needs and wants. This marketing material would be left behind after a call or with the receptionist to pass along to the appropriate person. Looking for something that is eye catching that in a glance could tell someone who we are and what we do. Our website is www.torvikltd-example.com. I attached our logo and powerpoint.

Target Market(s)

Manufacturing Companies or any company that does any type of shipping in North Americana.

Industry/Entity Type

Logistic

Requirements
Nice to have
• We would like the brochure to be a bi-fold.. I have attached a few examples I found on the internet

```html
<!DOCTYPE html>
<html lang="en">
<head>
<meta charset="utf-8">
<title>Torvik &amp; Associates – Dashboard Reporting &amp; Inbound Management</title>
<link rel="stylesheet" href="https://fonts.googleapis.com/css2?family=Open+Sans:wght@300;400;600&family=Roboto+Condensed:wght@700&family=Roboto+Slab:wght@300;400&display=swap">
<style>
  :root {
    --title-blue: #1f6fa8;
    --sky: #29a8e0;
    --navy: #1b4f82;
    --ink: #5d6166;
    --heading-ink: #55595e;
    --panel-line: #9aa5b0;
    --chart-blue: #2f77b8;
    --chart-green: #7cc36b;
    --chart-grey: #a7a9ac;
    --chart-purple: #8a4fa6;
    --chart-orange: #ef8a2c;
    --chart-teal: #57b9b0;
  }
  * { margin: 0; padding: 0; box-sizing: border-box; }
  html, body { width: 1200px; height: 848px; overflow: hidden; background: #ffffff; }
  .sheet {
    position: relative; width: 1200px; height: 848px; overflow: hidden;
    background: linear-gradient(180deg, #ffffff 0%, #f6f6f6 55%, #ececec 100%);
    font-family: "Roboto Slab", Georgia, serif;
  }
  .art { position: absolute; inset: 0; }
  .section-title {
    position: absolute; left: 34px;
    font-family: "Open Sans", Arial, sans-serif; font-weight: 400;
    font-size: 25px; letter-spacing: 0.3px; color: var(--title-blue);
  }
  .section-title.dashboard { top: 18px; }
  .section-title.inbound { top: 323px; }
  .dashboard-frame {
    position: absolute; left: 34px; top: 59px; width: 471px; height: 249px;
    border: 1px solid var(--panel-line); background: #fff;
  }
  .inbound-copy {
    position: absolute; left: 34px; top: 356px; width: 575px;
    font-size: 15.5px; font-weight: 300; line-height: 20.4px; color: var(--ink);
  }
  .inbound-copy h3 {
    font-family: "Roboto Condensed", "Arial Narrow", sans-serif; font-weight: 700;
    font-size: 16px; color: var(--heading-ink); margin-top: 7px;
  }
  .inbound-copy h3:first-child { margin-top: 0; }
  .inbound-copy h3 span { font-weight: 700; }
  .inbound-copy ul { list-style: none; }
  .inbound-copy li { text-indent: 15px; }
  .brand {
    position: absolute; left: 640px; top: 370px;
    display: flex; align-items: center; gap: 10px;
    font-family: "Open Sans", Arial, sans-serif; font-weight: 600;
    font-size: 25px; color: var(--navy); white-space: nowrap;
  }
  .brand .mark { width: 22px; height: 22px; background: var(--navy); }
</style>
</head>
<body>
<main class="sheet">

  <svg class="art" width="1200" height="848" viewBox="0 0 1200 848" aria-hidden="false">
    <defs>
      <linearGradient id="warehouseTeam" x1="0" y1="0" x2="1" y2="1">
        <stop offset="0" stop-color="#8a6b4e"/><stop offset="0.5" stop-color="#c9b49a"/><stop offset="1" stop-color="#9c7a55"/>
      </linearGradient>
      <linearGradient id="scannerWorker" x1="0" y1="0" x2="1" y2="1">
        <stop offset="0" stop-color="#b9a088"/><stop offset="0.6" stop-color="#d9cbbd"/><stop offset="1" stop-color="#a5927e"/>
      </linearGradient>
      <linearGradient id="tabletWorker" x1="0" y1="0" x2="1" y2="1">
        <stop offset="0" stop-color="#c7b29a"/><stop offset="0.5" stop-color="#e3d8cc"/><stop offset="1" stop-color="#b59874"/>
      </linearGradient>
      <linearGradient id="aisleTeam" x1="0" y1="0" x2="1" y2="1">
        <stop offset="0" stop-color="#9a5a3a"/><stop offset="0.45" stop-color="#c89a72"/><stop offset="1" stop-color="#4f6f96"/>
      </linearGradient>
    </defs>

    <polygon class="accent-band" points="884,8 1180,8 1168,44 876,44" fill="var(--sky)"/>

    <g role="img" aria-label="Photo: two colleagues checking a parcel with a tablet in a warehouse">
      <polygon points="520,8 872,8 846,292 520,292" fill="url(#warehouseTeam)"/>
    </g>
    <g role="img" aria-label="Photo: smiling worker scanning a box with a handheld scanner">
      <polygon points="822,54 1180,54 1180,322 792,322" fill="url(#scannerWorker)" stroke="#ffffff" stroke-width="8"/>
    </g>
    <g role="img" aria-label="Photo: warehouse worker using a tablet beside stacked boxes">
      <polygon points="874,324 1180,324 1180,534 858,534" fill="url(#tabletWorker)" stroke="#ffffff" stroke-width="8"/>
    </g>
    <g role="img" aria-label="Photo: two staff members reviewing stock in a tall shelving aisle">
      <polygon points="626,500 1180,500 1180,830 612,830" fill="url(#aisleTeam)" stroke="#ffffff" stroke-width="8"/>
    </g>

    <polygon class="brand-panel" points="570,298 856,298 842,444 552,444" fill="#ffffff"/>
    <polygon class="brand-band" points="552,440 850,440 842,482 546,482" fill="var(--navy)"/>
  </svg>

  <h2 class="section-title dashboard">Dashboard Reporting</h2>

  <div class="dashboard-frame">
    <svg width="469" height="247" viewBox="0 0 469 247" font-family="Open Sans, Arial, sans-serif">
      <g font-size="6.5" font-weight="600" fill="#333">
        <text x="6" y="10">Shipments in Transit</text>
        <text x="160" y="10">Shipments in Transit</text>
        <text x="315" y="10">All Shipments</text>
        <text x="6" y="130">All Shipments</text>
        <text x="160" y="130">Aging Report</text>
        <text x="315" y="130">Aging Report</text>
      </g>
      <g fill="none" stroke="#c7ccd1" stroke-width="0.8">
        <rect x="5" y="13" width="148" height="108"/><rect x="159" y="13" width="150" height="108"/><rect x="314" y="13" width="150" height="108"/>
        <rect x="5" y="133" width="148" height="108"/><rect x="159" y="133" width="150" height="108"/><rect x="314" y="133" width="150" height="108"/>
      </g>
      <g font-size="4.5" fill="#555" text-anchor="middle">
        <text x="79" y="21">All Shipments in Transit</text>
        <text x="234" y="21">In Transit Longer than 7 Days</text>
        <text x="389" y="21">Number of Booked Shipments</text>
        <text x="79" y="141">Number of Shipments by Carrier</text>
        <text x="234" y="141">Shipper Invoices</text>
        <text x="389" y="141">Past Due Invoices</text>
      </g>
      <!-- gauge -->
      <path d="M44 92 A35 35 0 0 1 114 92" fill="none" stroke="var(--chart-grey)" stroke-width="12"/>
      <path d="M58 64 A35 35 0 0 1 106 70" fill="none" stroke="var(--chart-green)" stroke-width="12"/>
      <path d="M106 70 A35 35 0 0 1 114 92" fill="none" stroke="var(--chart-blue)" stroke-width="12"/>
      <line x1="79" y1="92" x2="104" y2="88" stroke="#333" stroke-width="2"/>
      <circle cx="79" cy="92" r="3" fill="#333"/>
      <!-- bars -->
      <g fill="var(--chart-blue)">
        <rect x="186" y="80" width="24" height="27"/><rect x="222" y="34" width="24" height="73"/><rect x="258" y="62" width="24" height="45"/>
      </g>
      <line x1="180" y1="107" x2="296" y2="107" stroke="#999" stroke-width="0.6"/>
      <!-- stacked bars -->
      <rect x="338" y="58" width="22" height="32" fill="var(--chart-blue)"/><rect x="338" y="90" width="22" height="17" fill="var(--chart-green)"/>
      <rect x="376" y="40" width="22" height="34" fill="var(--chart-blue)"/><rect x="376" y="74" width="22" height="33" fill="var(--chart-green)"/>
      <rect x="414" y="72" width="22" height="27" fill="var(--chart-blue)"/><rect x="414" y="99" width="22" height="8" fill="var(--chart-green)"/>
      <line x1="332" y1="107" x2="448" y2="107" stroke="#999" stroke-width="0.6"/>
      <!-- donuts -->
      <g fill="none" stroke-width="14">
        <circle cx="79" cy="185" r="26" stroke="var(--chart-teal)"/>
        <path d="M79 159 A26 26 0 0 1 104 180" stroke="var(--chart-orange)"/>
        <path d="M104 180 A26 26 0 0 1 60 203" stroke="var(--chart-purple)"/>
        <path d="M79 159 A26 26 0 0 0 70 160" stroke="var(--chart-blue)"/>
        <circle cx="234" cy="185" r="26" stroke="var(--chart-blue)"/>
        <path d="M234 159 A26 26 0 0 0 208 183" stroke="var(--chart-green)"/>
        <circle cx="389" cy="185" r="26" stroke="var(--chart-blue)"/>
        <path d="M389 159 A26 26 0 0 0 364 178" stroke="var(--chart-green)"/>
      </g>
      <g font-size="5" fill="#333" text-anchor="middle">
        <text x="79" y="187">Total</text><text x="234" y="187">Total</text><text x="389" y="187">Total</text>
      </g>
    </svg>
  </div>

  <h2 class="section-title inbound">Inbound Management</h2>

  <section class="inbound-copy">
    <h3>Before IB Program</h3>
    <ul>
      <li>Little to no visibility to actual transportation costs</li>
      <li>Individual and non-integrated data, systems, processes</li>
      <li>Manual tracking or follow up – too many dependencies</li>
      <li>Constant monitoring – everyone is responsible</li>
      <li>Vendor Compliance either lacking or non-existent</li>
    </ul>
    <h3>After IB Program</h3>
    <ul>
      <li>Cost optimization throughout the supply chain</li>
      <li>Problems can be identified, tracked and minimized</li>
      <li>Centralized data, systems and processes</li>
      <li>Fully integrated platform provide continuity across the supply chain</li>
      <li>Systematically identify and communicate exceptions</li>
      <li>Increased Vendor Compliance (VIC Program)</li>
    </ul>
    <h3>Support Plan (outsourced offering)</h3>
    <ul>
      <li>Handle any questions and/or provide shipping instructions to all vendors</li>
      <li>Client and vendors will be provided with contact information to handle any questions</li>
      <li>Any issues will be immediately relayed to the appropriate contact at Client</li>
      <li>Follow-up plans will be immediately scheduled: In no way will service or vendor relations be compromised</li>
    </ul>
  </section>

  <div class="brand"><span class="mark"></span>Torvik &amp; Associates</div>

</main>
</body>
</html>
```